Images and design ideas provided: Postcard size flier

2 sided postcard size flier to hand people on the street.

A FUN tax business needs a postcard size flier to hand people on the street. Not a typical serious, quiet, office so make the image fun!

Exact wording, logo and key images provided. You are free to add other images as you see fit (such as money).

Side 1: Use image of lady looking up (she should be looking at text provided).All spanish and english text provided. Logo in bottom right corner. Address at bottom of card.

Side 2: Image of lady holding money and pointing. Remove money and have her holding a sign/or some other creative way to have her looking at text. All spanish and english text provided. Logo in bottom right corner. Address at bottom of card.

Size: 4" x 6" horizontal or vertical is ok
Each side can be different and image/design does not have to be related.

Target Market(s)

Age 18-35

Industry/Entity Type

Accounting

Font styles to use
Sans Serif

Colors

Designer to choose colors to be used in the design.

Requirements
Must have
• Use text document provided. All text goes on both sides.
• Should be easy to read from a few feet away.
Nice to have
• Bright colors to attract attention of people walking by to grab flier/card. Images of money ok.
Should not have
• No images of calculators or typical accounting tax forms.

```html
<!DOCTYPE html>
<html lang="en">
<head>
<meta charset="utf-8">
<title>Sunbeam Tax Co. – Postcard Fliers</title>
<link rel="stylesheet" href="https://fonts.googleapis.com/css2?family=Montserrat:wght@700;800;900&display=swap">
<style>
  :root {
    --stage: #2a2a2a;
    --card: #ffffff;
    --pattern-a: #f4f4f4;
    --pattern-b: #e6e6e6;
    --red: #c8202a;
    --red-dark: #8f1219;
    --blue: #2f6fbd;
    --blue-dark: #1f4f95;
    --yellow: #f6ee1c;
    --white: #ffffff;
    --ink: #222222;
    --robe-a: #7c8a5a;
    --robe-b: #b9a77a;
  }
  * { box-sizing: border-box; margin: 0; padding: 0; }
  html, body {
    width: 1200px; height: 1000px; overflow: hidden;
    background: var(--stage);
    font-family: "Montserrat", Arial, sans-serif;
  }
  .canvas { position: relative; width: 1200px; height: 1000px; }

  .postcard {
    position: absolute;
    background: var(--card);
    overflow: hidden;
    box-shadow: 0 10px 30px rgba(0,0,0,.45);
  }
  .postcard--landscape { left: 30px; top: 60px; width: 700px; height: 490px; }
  .postcard--portrait { left: 750px; top: 230px; width: 420px; height: 700px; }

  .crown-pattern {
    position: absolute; inset: 0;
    background: linear-gradient(160deg, var(--pattern-a), var(--pattern-b));
  }

  /* headline bands */
  .headline { position: absolute; color: var(--white); text-transform: uppercase; }
  .headline .band-en {
    background: linear-gradient(180deg, var(--red), var(--red-dark));
    clip-path: polygon(3% 0, 100% 0, 97% 100%, 0 100%);
    text-align: center;
  }
  .headline .band-es {
    background: linear-gradient(180deg, var(--blue), var(--blue-dark));
    clip-path: polygon(3% 0, 100% 0, 97% 100%, 0 100%);
    text-align: center;
  }
  .headline .cash-line { font-weight: 900; line-height: 1; display: block; text-shadow: 2px 2px 0 rgba(0,0,0,.35); }
  .headline .sub-line { font-weight: 800; line-height: 1.1; display: block; }
  .headline .amount { color: var(--yellow); }

  .postcard--landscape .headline {
    left: 185px; top: 28px; width: 500px;
    transform: rotate(-4deg);
  }
  .postcard--landscape .band-en { padding: 12px 18px 12px; }
  .postcard--landscape .band-en .cash-line { font-size: 40px; }
  .postcard--landscape .band-en .sub-line { font-size: 23px; margin-top: 4px; }
  .postcard--landscape .band-es { width: 420px; margin-left: 60px; padding: 7px 14px; }
  .postcard--landscape .band-es .cash-line { font-size: 19px; }
  .postcard--landscape .band-es .sub-line { font-size: 11px; margin-top: 2px; }

  /* sign held in portrait card */
  .held-sign {
    position: absolute; left: 20px; top: 240px; width: 380px; height: 145px;
    background: var(--white);
    box-shadow: 0 4px 10px rgba(0,0,0,.25);
  }
  .postcard--portrait .headline { left: 12px; top: 10px; width: 356px; }
  .postcard--portrait .band-en { padding: 7px 10px; }
  .postcard--portrait .band-en .cash-line { font-size: 25px; }
  .postcard--portrait .band-en .sub-line { font-size: 15px; margin-top: 2px; }
  .postcard--portrait .band-es { width: 300px; margin-left: 40px; margin-top: 6px; padding: 5px 8px; }
  .postcard--portrait .band-es .cash-line { font-size: 14px; }
  .postcard--portrait .band-es .sub-line { font-size: 8px; margin-top: 1px; }

  /* photo areas */
  .photo {
    position: absolute;
    background: linear-gradient(180deg, #d9b24a 0%, #c9463e 18%, var(--robe-b) 38%, var(--robe-a) 100%);
  }
  .postcard--landscape .photo { left: 55px; top: 180px; width: 360px; height: 310px; border-radius: 40% 40% 0 0; }
  .postcard--portrait .photo--upper { left: 120px; top: 30px; width: 180px; height: 215px; border-radius: 45% 45% 10% 10%;
    background: linear-gradient(180deg, #d63a33 0%, #d9b24a 45%, #d9a88a 100%); }
  .postcard--portrait .photo--lower { left: 80px; top: 385px; width: 260px; height: 110px;
    background: linear-gradient(180deg, var(--robe-b), var(--robe-a)); }

  /* brand plate */
  .brand-plate {
    position: absolute;
    display: flex; align-items: center; gap: 12px;
    background: var(--white);
    border: 3px solid var(--ink);
    border-radius: 6px;
    box-shadow: 0 3px 6px rgba(0,0,0,.25);
  }
  .brand-plate .brand-mark { background: var(--blue); border-radius: 50%; flex: none; }
  .brand-plate .brand-name { color: var(--blue-dark); font-weight: 800; line-height: 1.05; text-transform: uppercase; white-space: nowrap; }
  .postcard--landscape .brand-plate { left: 390px; top: 320px; width: 290px; height: 74px; padding: 0 18px; }
  .postcard--landscape .brand-mark { width: 40px; height: 40px; }
  .postcard--landscape .brand-name { font-size: 22px; }
  .postcard--portrait .brand-plate { left: 40px; top: 505px; width: 340px; height: 100px; padding: 0 24px; }
  .postcard--portrait .brand-mark { width: 54px; height: 54px; }
  .postcard--portrait .brand-name { font-size: 29px; }

  /* footer bands */
  .footer-bands { position: absolute; left: 0; bottom: 0; width: 100%; }
  .footer-bands svg { display: block; }
  .address {
    position: absolute; color: var(--white); font-weight: 700; white-space: nowrap;
  }
  .postcard--landscape .address { right: 20px; bottom: 20px; font-size: 13px; }
  .postcard--portrait .address { left: 22px; bottom: 26px; font-size: 13px; }
</style>
</head>
<body>
<main class="canvas">

  <!-- Side 1: landscape -->
  <section class="postcard postcard--landscape" aria-label="Postcard side one">
    <div class="crown-pattern" role="img" aria-label="Faint repeating crown pattern background"></div>

    <div class="footer-bands">
      <svg width="700" height="120" viewBox="0 0 700 120">
        <polygon points="0,80 700,40 700,120 0,120" fill="var(--red)"/>
        <polygon points="0,100 700,60 700,120 0,120" fill="var(--blue)"/>
      </svg>
    </div>

    <div class="photo" role="img" aria-label="Woman in a royal robe and crown hat looking up joyfully with arms raised"></div>

    <div class="headline">
      <div class="band-en">
        <span class="cash-line">Get <span class="amount">$100</span> Cash Now!</span>
        <span class="sub-line">With Paid Tax Preparation</span>
      </div>
      <div class="band-es">
        <span class="cash-line">Reciba <span class="amount">$100</span> en efectivo ahora!</span>
        <span class="sub-line">Con la preparacion pagada de sus impuestos</span>
      </div>
    </div>

    <div class="brand-plate">
      <span class="brand-mark"></span>
      <span class="brand-name">Sunbeam<br>Tax Co.</span>
    </div>

    <p class="address">418 Maple Ave. Bronx NY 10455 (718) 555-0147</p>
  </section>

  <!-- Side 2: portrait -->
  <section class="postcard postcard--portrait" aria-label="Postcard side two">
    <div class="crown-pattern" role="img" aria-label="Faint repeating crown pattern background"></div>

    <div class="photo photo--upper" role="img" aria-label="Smiling woman wearing a red and gold crown hat"></div>
    <div class="photo photo--lower" role="img" aria-label="Hands in a royal robe holding the sign"></div>

    <div class="held-sign">
      <div class="headline">
        <div class="band-en">
          <span class="cash-line">Get <span class="amount">$100</span> Cash Now!</span>
          <span class="sub-line">With Paid Tax Preparation</span>
        </div>
        <div class="band-es">
          <span class="cash-line">Reciba <span class="amount">$100</span> en efectivo ahora!</span>
          <span class="sub-line">Con la preparacion pagada de sus impuestos</span>
        </div>
      </div>
    </div>

    <div class="footer-bands">
      <svg width="420" height="90" viewBox="0 0 420 90">
        <polygon points="0,0 420,24 420,90 0,90" fill="var(--red)"/>
        <polygon points="0,18 420,40 420,90 0,90" fill="var(--blue)"/>
      </svg>
    </div>

    <div class="brand-plate">
      <span class="brand-mark"></span>
      <span class="brand-name">Sunbeam<br>Tax Co.</span>
    </div>

    <p class="address">418 Maple Ave. Bronx NY 10455 (718) 555-0147</p>
  </section>

</main>
</body>
</html>
```